Door Hanger Design for Electricians Serving Homes

I would like our logo incorporated into the door hanger. We would like a place for a tear off section on the bottom of the hanger with our contact information: K&T Electric - (555) 318-4702 - www.kandtelectric.example - info@kandtelectric.example.
Door Hanger Script
Front Side of the Door Hanger:
[Company Logo]
Need a Reliable Electrician?
Your Local Electrical Expert is Just Around the Corner!
• Quick Response Times
• Affordable Rates
• Quality Workmanship
• Fully Licensed & Insured
• Special Offer:
• 10% OFF Your First Service Call!
Back Side of the Door Hanger:
Don't Let Electrical Issues Keep You in the Dark!
From flickering lights to complete system upgrades, we've got all your
residential electrical needs covered. Our services include:
• Electrical Repairs & Troubleshooting
• Lighting Installation & Upgrades
• Safety Inspections & Code Compliance
• Energy-Efficient Solutions
• 24/7 Emergency Services
• Why Choose Us?
• Friendly, Local Service
• Over 30 Years of Experience
• Satisfaction Guaranteed
• Upfront Pricing
Call Us Today: [Your Phone Number]
Visit Our Website: [Your Website]
Book Your Appointment Now and Claim Your 10% Discount!
Offer valid for new customers on the first visit only. Mention this door hanger when
booking.
[Your Company Name and Contact Information]
Follow Us on Social Media for More Tips and Special Offers!
[Icons for social media platforms: Chatterpage, Pixmosaic, Quibbler, etc.]
Design Tips:
Use bold, clear fonts for easy reading.
Incorporate your brand colors and logo for instant recognition.
Include a clear call to action (CTA) on both sides.
Add a tear-off section at the bottom with your contact information for
convenience.
Use high-quality images or graphics related to electrical work to catch
the eye.
This door hanger design and copy aim to attract residential clients by
highlighting the benefits of your electrical services, special offers, and
how they can easily get in touch with you for their electrical needs.
The door knocker template will have three of the same design on front and three of the same design on the back. This template is from the print shop.

```html
<!DOCTYPE html>
<html lang="en">
<head>
<meta charset="utf-8">
<title>K&amp;T Electric Door Hanger</title>
<link href="https://fonts.googleapis.com/css2?family=Poppins:wght@400;500;600;700&display=swap" rel="stylesheet">
<style>
:root{
  --stage:#cbcbcc;
  --red:#e31e26;
  --dark:#3b3838;
  --white:#ffffff;
  --ink:#111111;
  --muted:#dcdcdc;
}
*{box-sizing:border-box;margin:0;padding:0}
html,body{width:1200px;height:848px;overflow:hidden;background:var(--stage);font-family:'Poppins',sans-serif}
.canvas{position:relative;width:1200px;height:848px}
.side-label{position:absolute;top:38px;width:268px;text-align:center;font-size:34px;font-weight:500;color:var(--ink)}
.hanger{position:absolute;top:100px;width:268px;height:648px;border-radius:30px 30px 24px 24px;overflow:hidden}
.hanger--front{left:302px;background:var(--white)}
.hanger--back{left:641px;background:var(--red)}
.hanger__shape{position:absolute;inset:0}
.abs{position:absolute}
.center{left:0;right:0;text-align:center}

/* front */
.brand{top:136px;font-size:15px;font-weight:700;color:var(--ink);display:flex;justify-content:center;align-items:center;gap:6px}
.brand__dot{width:10px;height:10px;background:var(--red);border-radius:50%}
.front__question{top:178px;font-size:12.5px;font-weight:700;color:var(--red)}
.front__photo{left:43px;top:225px;width:182px;height:182px;border-radius:50%;border:5px solid var(--white);background:radial-gradient(circle at 45% 40%,#8a8f98,#4d525a 60%,#2f3238)}
.badge{width:62px;height:62px;border-radius:50%;background:var(--white);border:3px solid var(--red);color:var(--red);display:flex;flex-direction:column;align-items:center;justify-content:center;line-height:1;font-weight:700}
.badge__big{font-size:18px}
.badge__small{font-size:12px}
.front__badge{left:26px;top:369px}
.front__headline{top:442px;left:20px;right:20px;font-size:13px;font-weight:500;color:var(--white);line-height:1.3}
.perks{top:488px;left:64px;list-style:none;font-size:8.8px;color:var(--white);line-height:13.4px}
.perks li::before{content:"";display:inline-block;width:5px;height:5px;background:var(--white);transform:rotate(45deg);margin-right:9px;vertical-align:1px}

/* shared footer */
.contact-pill{left:27px;width:214px;top:594px;height:25px;border-radius:13px;background:var(--white);font-size:13px;font-weight:600;color:var(--ink);display:flex;align-items:center;justify-content:center}
.contact-line{top:626px;font-size:7px;color:var(--white)}

/* back */
.back__intro{top:144px;left:22px;right:18px;font-size:9.8px;color:var(--white);line-height:1.4}
.back__intro strong{font-weight:700}
.section-title{font-size:11.5px;font-weight:700;color:var(--white)}
.section-title span{text-decoration:underline;text-underline-offset:3px}
.services{top:252px;left:34px;list-style:none;font-size:9.5px;color:var(--white);line-height:18px}
.services li::before{content:"";display:inline-block;width:8px;height:8px;border-radius:50%;background:var(--white);margin-right:13px;vertical-align:0}
.offer-band{left:40px;right:0;top:459px;height:25px;background:var(--white);color:var(--red);font-size:9.8px;font-weight:500;line-height:1.15;padding-left:38px;display:flex;align-items:center}
.back__badge{left:15px;top:445px;width:50px;height:50px}
.back__badge .badge__big{font-size:15px}
.back__badge .badge__small{font-size:10px}
.social{left:24px;width:221px;top:534px;display:grid;grid-template-columns:repeat(3,1fr)}
.social__name{background:var(--red);color:var(--white);font-size:8.5px;font-weight:600;text-align:center;height:16px;line-height:16px}
.social__mark{height:26px;display:flex;align-items:center;justify-content:center;border-right:1px solid var(--muted)}
.social__mark:last-child{border-right:none}
.social__mark i{display:block;width:13px;height:13px;border-radius:50%;background:var(--white)}
</style>
</head>
<body>
<div class="canvas">
  <div class="side-label" style="left:302px">Front Side</div>
  <div class="side-label" style="left:641px">Back Side</div>

  <!-- front -->
  <section class="hanger hanger--front">
    <svg class="hanger__shape" viewBox="0 0 268 648" aria-hidden="true">
      <path d="M0 242 Q120 200 268 222 L268 648 L0 648 Z" fill="var(--red)"/>
      <path d="M0 590 Q130 565 268 578 L268 648 L0 648 Z" fill="var(--dark)"/>
      <circle cx="134" cy="40" r="26" fill="var(--stage)"/>
      <path d="M150 24 L178 0 L190 0 L160 34 Z" fill="var(--stage)"/>
    </svg>
    <div class="abs center brand"><span class="brand__dot"></span>K&amp;T Electric</div>
    <div class="abs center front__question">NEED A RELIABLE ELECTRICIAN?</div>
    <div class="abs front__photo" role="img" aria-label="Photo of an electrician testing a wiring panel with a multimeter"></div>
    <div class="abs badge front__badge"><span class="badge__big">10%</span><span class="badge__small">OFF</span></div>
    <p class="abs center front__headline">Your Local Electrical Expert is Just Around the Corner!</p>
    <ul class="abs perks">
      <li>Quick Response Times</li>
      <li>Affordable Rates</li>
      <li>Quality Workmanship</li>
      <li>Fully Licensed &amp; Insured</li>
      <li>Special Offer</li>
      <li>10% OFF Your First Service Call!</li>
    </ul>
    <div class="abs contact-pill">K&amp;T Electric - (555) 318-4702</div>
    <div class="abs center contact-line">www.kandtelectric.example - info@kandtelectric.example</div>
  </section>

  <!-- back -->
  <section class="hanger hanger--back">
    <svg class="hanger__shape" viewBox="0 0 268 648" aria-hidden="true">
      <path d="M0 222 Q130 195 268 215 L268 588 Q130 602 0 590 Z" fill="var(--dark)"/>
      <circle cx="134" cy="40" r="26" fill="var(--stage)"/>
      <path d="M150 24 L178 0 L190 0 L160 34 Z" fill="var(--stage)"/>
    </svg>
    <p class="abs back__intro"><strong>Don't Let Electrical Issues Keep You in the Dark!</strong><br>From flickering lights to complete system upgrades, we've got all your</p>
    <div class="abs center section-title" style="top:222px"><span>Our services</span> include</div>
    <ul class="abs services">
      <li>Electrical Repairs &amp; Troubleshooting</li>
      <li>Lighting Installation &amp; Upgrades</li>
      <li>Safety Inspections &amp; Code Compliance</li>
      <li>Energy-Efficient Solutions</li>
      <li>24/7 Emergency Services</li>
      <li>Why Choose Us?</li>
      <li>Friendly, Local Service</li>
      <li>Over 30 Years of Experience</li>
      <li>Satisfaction Guaranteed</li>
      <li>Upfront Pricing</li>
    </ul>
    <div class="abs offer-band">Book Your Appointment Now<br>and Claim Your 10% Discount!</div>
    <div class="abs badge back__badge"><span class="badge__big">10%</span><span class="badge__small">OFF</span></div>
    <div class="abs center section-title" style="top:506px;font-size:10px"><span>Our social media platforms</span></div>
    <div class="abs social">
      <div class="social__name">Chatterpage</div>
      <div class="social__name">Quibbler</div>
      <div class="social__name">Pixmosaic</div>
      <div class="social__mark"><i></i></div>
      <div class="social__mark"><i></i></div>
      <div class="social__mark"><i></i></div>
    </div>
    <div class="abs contact-pill">K&amp;T Electric - (555) 318-4702</div>
    <div class="abs center contact-line">www.kandtelectric.example - info@kandtelectric.example</div>
  </section>
</div>
</body>
</html>
```